WP website design (Velmorte)

We need a wordpress design that will incorporate a professional color scheme with company logo in a clean layout. The design needs to consider that this will be developed on a responsive theme. Colors are undetermined - can use darker blue - logo is blue so creative use of colors will be important. Client wants a 'modern' look.

Industry/Entity Type

It Company

Font styles to use
Serif
Sans Serif

Colors

Designer to choose colors to be used in the design.

Requirements
Must have
• Navigation: 1) Home 2) Upcoming Auctions 3) For Sale 4) Sellers 5) About Us 6) Services 7) Gavel Caravan 8) Contact Us

Client mentions liking the look of the following site which can be used as inspiration: http://www.dorvankeel.example/professionals/tomas-reyley For the homepage txt, please use the content at http://www.velmorteauctions.example/ and place auction list below as seen at http://www.samplebidpage.example.host42-07.zone3-2.previewnode.example/auctions/

Site will have a slideshow element and the following widgets: 1) Featured Auctions 2) Testimonials blog widget 3) 'Auction Alerts' email sign up 4) Social Media icons (Chirpbook, Flitter, WorkLattice, ReelCast).
In the footer, there will be smaller company logo, the affiliations logo, and contact info below:
VELMORTE AUCTIONS
2738 Pelican Crest Blvd
Dania, Florida 33917
AB 471 • AU 638

TELEPHONE: (954) 555-0147 • FAX: (954) 555-0193
TOLL FREE: (800) 555-LOTS
info@velmorteauctions.example
Nice to have
• Use of drop-sown menu styling would be nice.

```html
<!DOCTYPE html>
<html lang="en">
<head>
<meta charset="utf-8">
<title>Velmorte Auctions</title>
<link href="https://fonts.googleapis.com/css2?family=Exo+2:wght@400;500&family=Open+Sans:wght@400;600&display=swap" rel="stylesheet">
<style>
:root{
  --blue:#0f4f9e;--blue-dark:#0b3f80;--red:#c8141c;--red-dark:#b40f16;
  --text:#555;--dark:#222;--link:#1a66b8;--panel:#e4e4e4;--line:#d2d2d2;--white:#fff;
}
*{margin:0;padding:0;box-sizing:border-box}
html,body{width:713px;height:1200px;overflow:hidden;background:var(--white);font-family:"Open Sans",sans-serif;color:var(--text)}
.page{position:relative;width:713px;height:1200px}
.topline{position:absolute;top:0;left:0;width:713px;height:3px;background:var(--red)}
.logo{position:absolute;left:59px;top:12px;width:110px;height:45px;border:2px solid var(--blue);display:flex;align-items:center;justify-content:center;gap:5px;font:500 17px "Exo 2",sans-serif;color:var(--blue);letter-spacing:.5px}
.logo span.dot{width:8px;height:8px;background:var(--red)}
.call{position:absolute;right:60px;top:18px;text-align:right;font-family:"Exo 2",sans-serif}
.call small{display:block;color:#e8a23a;font-size:11px}
.call b{font-weight:400;color:#3d6f9e;font-size:16px}
.nav{position:absolute;top:66px;left:0;width:713px;height:31px;background:var(--blue);display:flex;padding-left:59px}
.nav a{color:var(--white);font-size:8px;text-decoration:none;display:flex;align-items:center;justify-content:center;border-right:1px solid var(--blue-dark);height:31px}
.nav a:first-child{border-left:1px solid var(--blue-dark)}
.hero{position:absolute;top:97px;left:0;width:713px;height:283px;background:linear-gradient(180deg,#1c1a18 0%,#3a2d22 55%,#9a5a2a 82%,#5c3418 100%)}
.hero .label{position:absolute;left:59px;top:103px;width:138px;height:48px;background:var(--red);color:var(--white);font:400 19px "Exo 2",sans-serif;display:flex;align-items:center;justify-content:center}
.hero svg.arrow{position:absolute;top:118px}
.dots{position:absolute;top:261px;left:343px;display:flex;gap:5px}
.dots i{width:7px;height:7px;border-radius:50%;background:var(--white);border:1px solid #888}
.dots i.on{background:var(--red)}
.main{position:absolute;left:59px;top:392px;width:419px}
.main h1{font:400 14px "Exo 2",sans-serif;color:var(--blue)}
.main h1 em{font-style:normal;color:var(--red)}
.intro{margin-top:8px;font-size:7.2px;line-height:14.3px;color:var(--text)}
.bar{height:30px;margin-top:10px;background:linear-gradient(var(--red),var(--red-dark));color:var(--white);font:400 11px "Exo 2",sans-serif;display:flex;align-items:center;padding-left:8px;border-bottom:1px solid #9c0c12}
.item{position:absolute;left:0;width:419px;height:150px}
.item .photo{position:absolute;left:0;top:0;width:161px;height:149px}
.item .body{position:absolute;left:169px;top:5px;width:250px}
.item h2{font:400 10.5px "Exo 2",sans-serif;color:var(--link);line-height:14px;text-transform:uppercase}
.item .by{font-size:6.8px;color:var(--dark);margin-top:4px}
.item p{font-size:6.8px;line-height:14.3px;margin-top:6px;color:var(--text)}
.item .tools{display:flex;gap:12px;margin-top:6px;font-size:6.8px;color:var(--dark);align-items:center}
.tools span{display:flex;align-items:center;gap:4px}
.pager{position:absolute;left:323px;top:1081px;display:flex;gap:6px;align-items:center}
.pager b{width:18px;height:18px;border:1px solid #ccc;font:400 8px "Open Sans",sans-serif;display:flex;align-items:center;justify-content:center;color:var(--dark)}
.pager b.on{background:var(--blue);color:var(--white);border-color:var(--blue)}
.side{position:absolute;left:492px;width:161px}
.side .head{height:28px;background:linear-gradient(var(--red),var(--red-dark));color:var(--white);font:400 11px "Exo 2",sans-serif;display:flex;align-items:center;padding-left:10px}
.side .box{background:var(--panel);border:1px solid var(--line);border-top:0}
.avatar{width:48px;height:48px;border-radius:50%;margin:7px auto 0;background:radial-gradient(circle,#c99a7a,#7a5a48)}
.quote{font-size:7px;line-height:14.3px;text-align:center;padding:5px 10px 0;color:var(--dark)}
.who{font-size:6.5px;text-align:right;padding:4px 10px 8px;color:var(--dark)}
.socials{display:flex;gap:10px;padding:8px 12px;justify-content:flex-start}
.socials span{width:28px;height:28px;border-radius:5px;background:#3a5c8c;color:var(--white);font-size:4.6px;display:flex;align-items:center;justify-content:center}
.form{padding:8px 7px}
.form div{background:var(--white);border:1px solid #ccc;font-size:6.8px;color:#888;padding:0 8px;display:flex;align-items:center;height:21px;margin-bottom:11px}
.form div.msg{height:78px;align-items:flex-start;padding-top:6px}
.send{width:71px;height:20px;background:var(--blue);color:var(--white);font-size:8px;display:flex;align-items:center;padding-left:9px;gap:14px}
.footer{position:absolute;left:0;top:1125px;width:713px;height:75px;background:var(--blue);color:var(--white)}
.addr{position:absolute;left:59px;top:10px;font-size:7px;line-height:14.3px}
.badges{position:absolute;left:318px;top:15px;display:flex;gap:4px}
.badges i{width:38px;height:38px;background:var(--white);border:2px solid #dfe6ef}
.copy{position:absolute;right:61px;top:26px;text-align:right;font-size:7px;line-height:14.3px}
</style>
</head>
<body>
<div class="page">
  <div class="topline"></div>
  <div class="logo"><span class="dot"></span>Velmorte</div>
  <div class="call"><small>Call Us Today</small><b>(954) 555-0147</b></div>

  <nav class="nav">
    <a style="width:67px">Home</a><a style="width:86px">Upcoming Auctions</a><a style="width:58px">For Sale</a><a style="width:59px">Sellers</a><a style="width:60px">About Us</a><a style="width:66px">Services</a><a style="width:100px">Gavel Caravan</a><a style="width:88px">Contact Us</a>
  </nav>

  <div class="hero" role="img" aria-label="Golden scales of justice and a wooden gavel on a desk before shelves of law books">
    <div class="label">Auctions</div>
    <svg class="arrow" style="left:22px" width="14" height="22" viewBox="0 0 14 22"><path d="M11 2 3 11l8 9" fill="none" stroke="#fff" stroke-width="3.5"/></svg>
    <svg class="arrow" style="left:678px" width="14" height="22" viewBox="0 0 14 22"><path d="M3 2l8 9-8 9" fill="none" stroke="#fff" stroke-width="3.5"/></svg>
    <div class="dots"><i class="on"></i><i></i><i></i></div>
  </div>

  <section class="main">
    <h1>Welcome to <em>Velmorte Auctions</em></h1>
    <p class="intro">Harlan Auctions Inc. is a full time auction company engaged in the marketing and sale of real estate and personal property by auction. The auctioneers with Harlan Auctions are licensed to do business in the States of Kentucky, and Indiana. Their clients include numerous individuals, attorneys, banks, municipal agencies and the U.S. Bankruptcy Court. The four principle auctioneers in the company have a combined 90 years of experience in the auction business.</p>
    <div class="bar">Auction Calendar</div>
  </section>

  <div style="position:absolute;left:59px;top:540px">
    <article class="item" style="top:0">
      <div class="photo" role="img" aria-label="Red car on a mountain road beside a rock cliff" style="background:linear-gradient(160deg,#8a8270,#5e6a58 45%,#b0aa9c)"></div>
      <div class="body">
        <h2>Benefit Auction – Riverbend Family Fund</h2>
        <div class="by">By Kenji Arimura Jun 19,2014 8.44 AM GMT+0530</div>
        <p>The report discloses that patient information was sold to 178 private firms on 588 occasions between 2005 and 2012, with sales to pharmaceutical companies and at least five major insurance provider The report discloses that patient information was sold to 178 private firms on 588 occasions between 2005 and 2012.</p>
        <div class="tools">
          <span><svg width="9" height="7" viewBox="0 0 9 7"><rect width="9" height="7" fill="#3a6fb0"/><path d="M0 0l4.5 4L9 0" fill="none" stroke="#fff"/></svg>Email Friends</span>
          <span><svg width="8" height="8" viewBox="0 0 8 8"><rect y="3" width="8" height="4" fill="#3a6fb0"/><rect x="2" width="4" height="3" fill="#3a6fb0"/></svg>Print</span>
          <span><svg width="9" height="8" viewBox="0 0 9 8"><path d="M0 0h9v5H4L1 8V5H0z" fill="#3a6fb0"/></svg>Comments</span>
          <span><svg width="8" height="8" viewBox="0 0 8 8"><path d="M0 3h2v5H0zM3 3l2-3h1v3h2v5H3z" fill="#3a6fb0"/></svg>Like</span>
        </div>
      </div>
    </article>
    <article class="item" style="top:177px">
      <div class="photo" role="img" aria-label="Brick house with a green lawn and trees" style="background:linear-gradient(180deg,#9cc4e8 0%,#6f8a5a 40%,#a06848 60%,#5a9a38 80%)"></div>
      <div class="body">
        <h2>Absolute Online Only Auction – Antiques and Collectibles</h2>
        <div class="by">By Kenji Arimura Jun 19,2014 8.44 AM GMT+0530</div>
        <p>The report discloses that patient information was sold to 178 private firms on 588 occasions between 2005 and 2012, with sales to pharmaceutical companies and at least five major insurance provider The report discloses that patient information was sold to 178 private firms on 588 occasions between 2005 and 2012.</p>
        <div class="tools">
          <span><svg width="9" height="7" viewBox="0 0 9 7"><rect width="9" height="7" fill="#3a6fb0"/><path d="M0 0l4.5 4L9 0" fill="none" stroke="#fff"/></svg>Email Friends</span>
          <span><svg width="8" height="8" viewBox="0 0 8 8"><rect y="3" width="8" height="4" fill="#3a6fb0"/><rect x="2" width="4" height="3" fill="#3a6fb0"/></svg>Print</span>
          <span><svg width="9" height="8" viewBox="0 0 9 8"><path d="M0 0h9v5H4L1 8V5H0z" fill="#3a6fb0"/></svg>Comments</span>
          <span><svg width="8" height="8" viewBox="0 0 8 8"><path d="M0 3h2v5H0zM3 3l2-3h1v3h2v5H3z" fill="#3a6fb0"/></svg>Like</span>
        </div>
      </div>
    </article>
    <article class="item" style="top:365px">
      <div class="photo" role="img" aria-label="Person in a dark robe holding law books and a gavel" style="background:linear-gradient(135deg,#1c1c1c,#3a2a22 50%,#6a4030)"></div>
      <div class="body">
        <h2>Absolute Online Only Auction – Personal Property</h2>
        <div class="by">By Kenji Arimura Jun 19,2014 8.44 AM GMT+0530</div>
        <p>The report discloses that patient information was sold to 178 private firms on 588 occasions between 2005 and 2012, with sales to pharmaceutical companies and at least five major insurance provider The report discloses that patient information was sold to 178 private firms on 588 occasions between 2005 and 2012.</p>
        <div class="tools">
          <span><svg width="9" height="7" viewBox="0 0 9 7"><rect width="9" height="7" fill="#3a6fb0"/><path d="M0 0l4.5 4L9 0" fill="none" stroke="#fff"/></svg>Email Friends</span>
          <span><svg width="8" height="8" viewBox="0 0 8 8"><rect y="3" width="8" height="4" fill="#3a6fb0"/><rect x="2" width="4" height="3" fill="#3a6fb0"/></svg>Print</span>
          <span><svg width="9" height="8" viewBox="0 0 9 8"><path d="M0 0h9v5H4L1 8V5H0z" fill="#3a6fb0"/></svg>Comments</span>
          <span><svg width="8" height="8" viewBox="0 0 8 8"><path d="M0 3h2v5H0zM3 3l2-3h1v3h2v5H3z" fill="#3a6fb0"/></svg>Like</span>
        </div>
      </div>
    </article>
  </div>

  <div class="pager">
    <svg width="9" height="9" viewBox="0 0 9 9"><path d="M8 0v9L0 4.5z" fill="#999"/></svg>
    <b class="on">1</b><b>2</b><b>3</b><b>4</b><b>5</b>
    <svg width="9" height="9" viewBox="0 0 9 9"><path d="M1 0v9l8-4.5z" fill="var(--blue)"/></svg>
  </div>

  <aside class="side" style="top:388px">
    <div class="head">Testimonals</div>
    <div class="box">
      <div class="avatar" role="img" aria-label="Customer portrait"></div>
      <p class="quote">Donec sed odio dui. Nullam id dolor id nibh ultricies vehicula ut id elit. Sollicitudin Lorem Egestas Dapibus. Fusce dapibus, tellus ac cursus commodo<br>“</p>
      <p class="who">Mr.Dale, Manager</p>
    </div>
  </aside>

  <aside class="side" style="top:581px">
    <div class="head">Socail</div>
    <div class="box socials">
      <span>Chirpbook</span><span style="background:#3a8ab0">Flitter</span><span style="background:#2c6ea0">WorkLattice</span><span style="background:#d0502a">ReelCast</span>
    </div>
  </aside>

  <aside class="side" style="top:670px">
    <div class="head">Featured Auctions widget</div>
    <div role="img" aria-label="Figure standing in the bright doorway of a worn room" style="height:141px;background:linear-gradient(90deg,#3c3c3c,#6a6a66 45%,#2a6a9a 70%,#1a2a3a);position:relative">
      <div class="dots" style="left:68px;top:127px"><i class="on" style="width:5px;height:5px;background:#e8a23a;border:0"></i><i style="width:5px;height:5px;border:0"></i><i style="width:5px;height:5px;border:0"></i></div>
    </div>
  </aside>

  <aside class="side" style="top:860px">
    <div class="head">Auction Alerts</div>
    <div class="box form">
      <div>Name</div>
      <div>Your email address</div>
      <div class="msg">Message</div>
      <span class="send">Send it <svg width="14" height="6" viewBox="0 0 14 6"><path d="M0 3h13M10 0l3 3-3 3" fill="none" stroke="#fff"/></svg></span>
    </div>
  </aside>

  <footer class="footer">
    <div class="addr">VELMORTE AUCTIONS<br>2738 Pelican Crest Blvd<br>Dania, Florida 33917<br>AB 471 • AU 638</div>
    <div class="badges"><i></i><i></i></div>
    <div class="copy">Copyright 2009. All rights reserved.<br>© Velmorte Auction Company</div>
  </footer>
</div>
</body>
</html>
```